Flyer Needed to Advertise New Online Reading Programs

ABOUT THE TRUST OF READING DEVELOPMENT
The Trust teaches summer reading skills programs for elementary school students, in programs offered through partnerships with universities, colleges and municipalities nationwide. The goal of each program is to build reading skills, and to foster a lifetime love of books and reading.

AIMS & TARGET MARKET
The Trust has developed a new format of its’ online reading program for elementary students, which includes live small-group video classes taught by a professional reading teacher. The Trust seeks a new graphic design for a flyer to advertise the new online reading program. The flyer will be sent to elementary schools, passed out by teachers, and then taken home by students to show parents; therefore, the primary audience for the flyer will be teachers and parents of elementary school students.

Live classes for children are completely new in online education, unlike anything else in the marketplace, and parents and teachers therefore have no experience with them. The successful design will include illustrations or photographs that allow visitors to immediately grasp/understand the new video class format, without relying heavily on a written description. Additionally, the successful flyer concept will make the program, and the video classes in particular, feel fun and appealing to kids and parents.

Below is additional information about the new live small-group video class format, which meets weekly for 6 weeks:
o During video classes, students participate from home.
o During discussions, the student’s computer (or tablet) screen is filled with live video frames of the teacher and the other students. The video frame for the teacher is larger, and the other students appear in smaller frames.
o During other video class instruction, the teacher uses a presentation screen to display pages of a book or a “whiteboard” used for instructional activities.

Notes: The flyer design could include an illustrated or photo screenshot of a video class, with children looking engaged and a teacher leading them in discussion (stock photos are okay to use in flyer design). We have included a screen shot of one of these classes for reference, but do not feel constrained to represent this screen realistically (as shown here). Layout, look and feel can be changed. Alternatively, you may choose to use a graphic other than a screenshot to bring across the concept of the video classes.

COPY AND SPECIFICATIONS
The flyer design will be one-sided and the dimensions are 8.5” x 11” in either portrait or landscape orientation. We will consider designs in color or black and white. Since we brand our flyers with logos of the universities we partner with throughout the nation, we’ll need to include a partner logo in the design. Exact copy will be provided, but layout is flexible. Screenshots from our sample classes are included to show screen layout. Stock photos are okay to use in flyer designs.

Reason: We'd like to make edits to existing designs.

Hi designers, We wanted to share our thoughts on the main image of the flyer. We're leaning towards an image that shows a sole student on a computer with the computer screen in view. The computer screen could have the sample image we provided to show how the video classes operate. Thanks! The Trust of Reading Development

Graphic Design

```html
<!DOCTYPE html>
<html lang="en">
<head>
<meta charset="utf-8">
<title>Reading Skills Classes — Online this Summer</title>
<link rel="stylesheet" href="https://fonts.googleapis.com/css2?family=Abril+Fatface&family=PT+Sans+Narrow:wght@400;700&family=Open+Sans:wght@300;400;700&display=swap">
<style>
  :root {
    --page: #ffffff;
    --ink: #ffffff;
    --ground-dark: #0c0c0c;
    --ground-mid: #2a2a2a;
    --panel-fill: rgba(70, 70, 70, 0.55);
    --panel-edge: #c8c8c8;
    --shot-top: #5a5550;
    --shot-bottom: #1b1d22;
    --shot-edge: #e6e6e6;
  }
  * { margin: 0; padding: 0; box-sizing: border-box; }
  html, body { width: 999px; height: 1200px; overflow: hidden; background: var(--page); }
  .flyer {
    position: relative; width: 999px; height: 1200px; background: var(--page);
    color: var(--ink); font-family: "PT Sans Narrow", "Arial Narrow", sans-serif;
  }
  .ground {
    position: absolute; left: 57px; top: 27px; width: 885px; height: 1145px;
    background: linear-gradient(90deg, var(--ground-dark) 0%, var(--ground-mid) 50%, var(--ground-dark) 100%);
  }
  .title {
    position: absolute; left: 76px; top: 40px;
    font-family: "Abril Fatface", Georgia, serif; font-weight: 400; line-height: 1;
  }
  .title-main { display: block; font-size: 128px; letter-spacing: 1px; }
  .title-sub { display: block; font-size: 56px; margin-top: -8px; margin-left: 8px; letter-spacing: 1px; }
  .partner {
    position: absolute; left: 628px; top: 67px; width: 280px; height: 121px;
    display: flex; flex-direction: column; align-items: center; justify-content: center;
    font-family: "Open Sans", Arial, sans-serif; font-weight: 400; font-size: 27px;
    line-height: 1.2; letter-spacing: 1px; text-align: center;
  }
  .panel {
    position: absolute; left: 80px; top: 225px; width: 837px; height: 785px;
    border: 3px solid var(--panel-edge); border-radius: 12px; background: var(--panel-fill);
  }
  .tagline {
    position: absolute; left: 93px; top: 232px;
    font-family: "Open Sans", Arial, sans-serif; font-weight: 300; font-size: 30px;
  }
  .highlights {
    position: absolute; left: 95px; top: 296px; list-style: none;
    font-weight: 700; font-size: 22px; line-height: 29.5px;
  }
  .highlights li::before { content: "•"; margin-right: 10px; }
  .class-screen {
    position: absolute; left: 592px; top: 238px; width: 296px; height: 200px;
    border: 3px solid var(--shot-edge); border-radius: 6px;
    background: linear-gradient(180deg, var(--shot-top) 0%, var(--shot-bottom) 100%);
  }
  .program { position: absolute; width: 358px; }
  .program h2 { font-weight: 700; font-size: 20px; line-height: 24px; margin-bottom: 6px; }
  .program p { font-size: 16.5px; line-height: 20.8px; text-align: justify; }
  .col-left { left: 99px; }
  .col-right { left: 540px; }
  .row-1 { top: 450px; }
  .row-2 { top: 605px; }
  .row-3 { top: 762px; }
  .program.wide { left: 99px; top: 906px; width: 808px; }
  .program.wide h2 { margin-bottom: 2px; }
  .program.wide p { text-align: left; }
  .footer {
    position: absolute; left: 57px; top: 1014px; width: 885px; text-align: center;
    font-family: "Open Sans", Arial, sans-serif;
  }
  .hours { font-size: 27px; font-weight: 400; line-height: 36px; }
  .register { font-size: 29px; font-weight: 400; line-height: 38px; }
  .phone { font-size: 58px; font-weight: 700; line-height: 70px; }
</style>
</head>
<body>
<div class="flyer">
  <div class="ground"></div>

  <h1 class="title">
    <span class="title-main">Reading</span>
    <span class="title-sub">Skills Classes</span>
  </h1>

  <div class="partner">WESTBROOK<br>UNIVERSITY</div>

  <div class="panel"></div>
  <p class="tagline">Online this Summer!</p>
  <ul class="highlights">
    <li>Small class size</li>
    <li>A skilled and encouraging teacher</li>
    <li>Individualized skills instruction</li>
    <li>A program of independent reading in great books</li>
  </ul>

  <div class="class-screen" role="img" aria-label="Screenshot of a live video class: a teacher with a headset in a large frame, small frames of students below"></div>

  <section class="program col-left row-1">
    <h2>Program for Preschoolers:</h2>
    <p>Students in this program build strong reading readiness skills. Your child will learn letter recognition and beginning phonics, and develop the motivation and love of reading that make learning to read easy, enjoyable, and successful.</p>
  </section>
  <section class="program col-right row-1">
    <h2>Program for Entering Kindergartners:</h2>
    <p>Students in this program learn beginning reading skills and develop a love of books. Your child will learn letter recognition, phonics, and sight words, and will learn to sound out short words.</p>
  </section>
  <section class="program col-left row-2">
    <h2>Program for Entering 1st Graders:</h2>
    <p>Students in this program learn to read independently. Your child will learn phonics and sight words, build comprehension, and gain the skills and confidence needed for success in first grade.</p>
  </section>
  <section class="program col-right row-2">
    <h2>Program for Entering 2nd Graders:</h2>
    <p>Students in this program become fluent, independent readers. Your child will make significant gains in phonics and word-attack skills, fluency, and comprehension, and will develop confidence and a love of reading.</p>
  </section>
  <section class="program col-left row-3">
    <h2>Program for Entering 3rd Graders:</h2>
    <p>Students in this program become strong independent readers. Your child will develop the comprehension, fluency, and long-word decoding skills needed to read longer books with ease, and will build confidence and a love of reading.</p>
  </section>
  <section class="program col-right row-3">
    <h2>Program for Entering 4th and 5th Graders:</h2>
    <p>Students in this program make substantial gains in comprehension, long-word decoding skills, fluency, and reading speed. Your child will complete homework more quickly and easily, be more successful in school, and become a strong, enthusiastic reader.</p>
  </section>
  <section class="program wide">
    <h2>Programs for Entering 6th-8th Graders and Entering 9th and 10th Graders:</h2>
    <p>Students in these programs make substantial gains in comprehension while doubling reading speed. They also learn the best way to read textbooks, take notes, and study for tests. As a result, students complete homework more quickly and easily, get better grades, and enjoy reading more.</p>
  </section>

  <footer class="footer">
    <p class="hours">Mon.-Fri. 5am–7pm, Sat. 5am–4pm and Sun. 6am–4pm</p>
    <p class="register">For More Information or to Register</p>
    <p class="phone">Call 1-800-555-0142</p>
  </footer>
</div>
</body>
</html>
```